Business Card Design

I'm a commercial general contractor remodel offices, hotels, health clubs and stores mostly San Francisco and the peninsula
the file I down loaded is kind of what I want I like the I beam with my company name in it, that would be fine with me but if you have better Idea will look at it you never know, I'm decided to give in and change my company name to how every one knows me, I have been in business since 1991, I like the I beam logo I included one of my old card from my old company for reference for you.

Industry/Entity Type

Business

Contact Information for Business Card

BRAXO CONSTRUCTION (is my company name)
Wendell Trusk contractor, LIc 314827
4158 Garnet Row, Ashford Vale, California 90417
mobile, (415) 555-0147
phone (650) 555-0182
Fax, (650) 555-0183
email, braxo@braxoconstruction.example

```html
<!DOCTYPE html>
<html lang="en">
<head>
<meta charset="UTF-8">
<title>Braxo Construction – Business Card</title>
<link rel="stylesheet" href="https://fonts.googleapis.com/css2?family=Josefin+Sans:wght@300;400;600&display=swap">
<style>
  :root {
    --page-bg: #2b2b2c;
    --card-dark: #141414;
    --card-mid: #2e2f30;
    --card-light: #4a4b4c;
    --accent: #f2a615;
    --accent-deep: #c8860c;
    --stripe-dark: #161616;
    --text-light: #e9e9e9;
    --panel: rgba(150, 150, 150, 0.45);
  }
  * { box-sizing: border-box; margin: 0; padding: 0; }
  html, body {
    width: 1200px;
    height: 900px;
    overflow: hidden;
    background: var(--page-bg);
    font-family: "Josefin Sans", sans-serif;
  }
  .canvas {
    position: relative;
    width: 1200px;
    height: 900px;
    display: flex;
    align-items: center;
    justify-content: center;
  }
  .card {
    position: relative;
    width: 1050px;
    height: 600px;
    overflow: hidden;
    background:
      radial-gradient(ellipse at 50% 40%, var(--card-light) 0%, var(--card-mid) 40%, var(--card-dark) 100%);
    color: var(--text-light);
  }
  .hazard-band {
    position: absolute;
    left: 0;
    width: 100%;
    height: 44px;
    background: linear-gradient(90deg, var(--stripe-dark) 0%, var(--accent-deep) 30%, var(--stripe-dark) 50%, var(--accent-deep) 75%, var(--stripe-dark) 100%);
  }
  .hazard-band--top { top: 26px; }
  .hazard-band--bottom { bottom: 26px; }
  .license {
    position: absolute;
    top: 110px;
    right: 60px;
    font-size: 20px;
    letter-spacing: 2px;
    font-weight: 400;
  }
  .company-name {
    position: absolute;
    top: 150px;
    left: 150px;
    display: flex;
    align-items: center;
    gap: 18px;
    font-size: 64px;
    font-weight: 400;
    letter-spacing: 2px;
    color: var(--accent);
    white-space: nowrap;
  }
  .company-name .mark {
    width: 22px;
    height: 22px;
    background: var(--accent);
  }
  .contractor-panel {
    position: absolute;
    top: 250px;
    left: 300px;
    width: 440px;
    height: 130px;
    background: var(--panel);
    text-align: center;
    padding-top: 14px;
  }
  .contractor-name {
    font-size: 26px;
    font-weight: 600;
    letter-spacing: 2px;
    text-transform: uppercase;
  }
  .contractor-role {
    font-size: 14px;
    letter-spacing: 2px;
    text-transform: uppercase;
    margin-bottom: 8px;
  }
  .address {
    font-size: 20px;
    line-height: 1.3;
    letter-spacing: 1px;
    text-transform: uppercase;
    font-style: normal;
  }
  .contact-list {
    position: absolute;
    left: 60px;
    top: 400px;
    list-style: none;
    font-size: 20px;
    line-height: 1.45;
    letter-spacing: 1px;
  }
  .contact-list .label { text-transform: uppercase; }
</style>
</head>
<body>
  <main class="canvas">
    <section class="card" aria-label="Braxo Construction business card">
      <div class="hazard-band hazard-band--top" role="img" aria-label="Yellow and black hazard stripe band"></div>

      <p class="license">LIC 314827</p>

      <h1 class="company-name"><span class="mark" aria-hidden="true"></span>BRAXO CONSTRUCTION</h1>

      <div class="contractor-panel">
        <p class="contractor-name">Wendell Trusk</p>
        <p class="contractor-role">Contractor</p>
        <address class="address">4158 Garnet Row, Ashford Vale,<br>California 90417</address>
      </div>

      <ul class="contact-list">
        <li><span class="label">Mobile:</span> (415) 555-0147</li>
        <li><span class="label">Phone:</span> (650) 555-0182</li>
        <li><span class="label">Fax:</span> (650) 555-0183</li>
        <li><span class="label">Email:</span> braxo@braxoconstruction.example</li>
      </ul>

      <div class="hazard-band hazard-band--bottom" role="img" aria-label="Yellow and black hazard stripe band"></div>
    </section>
  </main>
</body>
</html>
```